Educational Software Company Seeking Event Postcard Design

We are looking for a postcard promoting an upcoming event. We would like to utilize the red, white and blue color scheme that you will see on the site at: http://buildingcrafters.campuswren.example/ksx. Gray can also be used. Please feel free to add some extra design elements. This postcard is targeting education operations professionals.

7th Annual Northern New England Plantworks Summit Gathering

When: February 27th -28th

Where: Portsmouth, New Hampshire

Call to action - Register Today: linkhop.example/PSG-Register

I have attached a word containing the text I'd like you to use and an example template. Some design elements will need to be added to the template

Red = bf1e2d
Blue = 0054a6

Target Market(s)

education operations professionals

Industry/Entity Type

Education

Requirements
Must have
• Plantworks Summit Gathering logo, name of conference, date, location, blue, red, white and gray seen on website:

Red = bf1e2d
Blue = 0054a6

When: February 27th -28th

```html
<!DOCTYPE html>
<html lang="en">
<head>
<meta charset="utf-8">
<title>7th Annual Northern New England Plantworks Summit Gathering</title>
<link href="https://fonts.googleapis.com/css2?family=Josefin+Sans:wght@300;400&family=Montserrat:wght@600;700&display=swap" rel="stylesheet">
<style>
  :root {
    --brand-red: #bf1e2d;
    --band-red: #c9304a;
    --brand-blue: #0054a6;
    --gray: #555a60;
    --white: #ffffff;
  }
  * { margin: 0; padding: 0; box-sizing: border-box; }
  html, body { width: 1200px; height: 773px; overflow: hidden; background: var(--white); }
  .postcard {
    position: relative;
    width: 1200px;
    height: 773px;
    background: var(--white);
    font-family: "Josefin Sans", sans-serif;
  }
  .brand-mark {
    position: absolute;
    left: 62px;
    top: 120px;
    width: 278px;
    display: flex;
    align-items: center;
    gap: 14px;
    color: var(--brand-blue);
    font-size: 64px;
    font-weight: 400;
    letter-spacing: 2px;
  }
  .brand-mark .dot {
    width: 34px;
    height: 34px;
    border-radius: 50%;
    background: var(--brand-red);
    flex: none;
  }
  .headline {
    position: absolute;
    left: 421px;
    top: 100px;
    color: var(--brand-blue);
    font-weight: 300;
    font-variant: small-caps;
    line-height: 1;
  }
  .headline .edition { display: block; font-size: 96px; letter-spacing: 3px; }
  .headline .region,
  .headline .event-name { display: block; font-size: 48px; letter-spacing: 1.5px; margin-top: 10px; }
  .when-where {
    position: absolute;
    left: 423px;
    top: 330px;
    color: var(--brand-red);
    font-size: 25px;
    font-weight: 400;
    letter-spacing: 0.5px;
  }
  .cta-band {
    position: absolute;
    left: 0;
    top: 435px;
    width: 1200px;
    height: 81px;
    background: var(--band-red);
    display: flex;
    align-items: center;
    color: var(--white);
    font-family: "Montserrat", sans-serif;
    font-weight: 600;
  }
  .cta-band .cta { margin-left: 78px; font-size: 40px; letter-spacing: 2px; }
  .cta-band .cta-link { margin-left: 56px; font-size: 35px; letter-spacing: 0.5px; }
  .hosts-label {
    position: absolute;
    left: 398px;
    top: 578px;
    color: var(--gray);
    font-size: 25px;
    font-weight: 300;
    line-height: 1.2;
    letter-spacing: 1px;
  }
  .host {
    position: absolute;
    color: var(--brand-blue);
    font-family: "Josefin Sans", sans-serif;
    font-weight: 400;
    text-align: center;
    line-height: 1.15;
  }
  .host-granite { left: 634px; top: 640px; width: 150px; font-size: 15px; }
  .host-pine { left: 796px; top: 610px; width: 140px; font-size: 15px; }
  .host-campuswren { left: 960px; top: 640px; width: 130px; font-size: 24px; }
</style>
</head>
<body>
  <main class="postcard">
    <div class="brand-mark"><span class="dot"></span>PSG</div>

    <h1 class="headline">
      <span class="edition">7th Annual</span>
      <span class="region">Northern New England</span>
      <span class="event-name">Plantworks Summit Gathering</span>
    </h1>

    <p class="when-where">February 27th -28th in Portsmouth, New Hampshire</p>

    <div class="cta-band">
      <span class="cta">REGISTER TODAY</span>
      <span class="cta-link">linkhop.example/PSG-Register</span>
    </div>

    <p class="hosts-label">This conference is<br>proudly hosted by:</p>

    <p class="host host-granite">Granite Association of School Finance Officers</p>
    <p class="host host-pine">Pine Coast Association of School Finance Officers</p>
    <p class="host host-campuswren">CampusWren</p>
  </main>
</body>
</html>
```